Generic Post Card

New Product promotion. Attached is a card we did earlier. I made modifications to it so you can get an idea of what I want. The colors match our web page at ridgefoxparts.com

```html
<!DOCTYPE html>
<html lang="en">
<head>
<meta charset="utf-8">
<title>Nitrous Oxide Inhaler Postcard</title>
<link href="https://fonts.googleapis.com/css2?family=Oswald:wght@600&family=Lato:wght@400;700;900&display=swap" rel="stylesheet">
<style>
  :root{
    --stage:#8c8c8c;
    --blue:#2f5f9e;
    --blue-light:#4a8fc9;
    --orange:#f39a1e;
    --orange-light:#fbb53a;
    --yellow:#f7b318;
    --dark:#2b2b2b;
    --white:#ffffff;
    --photo-a:#cfd3cf;
    --photo-b:#9fae9e;
    --device-a:#f4f4f4;
    --device-b:#d9dde2;
  }
  *{margin:0;padding:0;box-sizing:border-box}
  html,body{width:900px;height:1200px;overflow:hidden;background:var(--stage)}
  body{position:relative;font-family:"Lato",Arial,sans-serif}
  .card{position:absolute;left:105px;width:690px;height:535px;background:var(--white);overflow:hidden}
  .card--front{top:42px}
  .card--back{top:622px}
  .card svg.art{position:absolute;inset:0}
  .txt{position:absolute;white-space:nowrap}
  .formula{right:60px;top:22px;font:900 44px/1 "Lato",sans-serif;color:var(--white)}
  .title{left:20px}
  .title--nitrous{top:95px;font:600 48px/1 "Oswald",sans-serif;color:var(--dark);text-transform:uppercase}
  .title--oxide{top:150px;font:400 48px/1 "Lato",sans-serif;color:var(--white)}
  .title--inhaler{top:202px;font:400 36px/1 "Lato",sans-serif;color:var(--dark)}
  .product-shot{position:absolute;left:24px;top:256px;width:96px;height:112px;border-radius:14px;background:linear-gradient(180deg,var(--device-a),var(--device-b))}
  .plus{left:136px;top:272px;font:900 40px/1 "Lato",sans-serif;color:var(--dark)}
  .painful{left:180px;top:272px;font:900 19px/1 "Lato",sans-serif;color:var(--blue)}
  .procedure{left:180px;top:297px;font:400 19px/1 "Lato",sans-serif;color:var(--dark)}
  .equals{left:326px;top:276px;font:900 36px/1 "Lato",sans-serif;color:var(--dark)}
  .reduce{left:20px;top:374px;font:900 22px/1 "Lato",sans-serif;color:var(--yellow)}
  .seconds{left:20px;top:402px;font:400 31px/1 "Lato",sans-serif;color:var(--white)}
  .contact{list-style:none;position:absolute;color:var(--white);font:700 13px/19px "Lato",sans-serif}
  .contact li{display:flex;align-items:center;gap:7px}
  .contact svg{width:13px;height:13px;flex:none}
  .contact--front{left:24px;top:464px}
  .ask{left:20px;top:40px;font:600 31px/1 "Oswald",sans-serif;color:var(--white)}
  .ask-sub{left:20px;top:80px;font:400 15px/1 "Lato",sans-serif;color:var(--dark)}
  .blurb{position:absolute;left:20px;top:372px;width:320px;font:400 15px/19px "Lato",sans-serif;color:var(--dark)}
  .benefits{left:20px;top:422px;font:700 33px/1 "Lato",sans-serif;color:var(--dark);display:flex;gap:12px}
  .benefits span{display:flex;align-items:center;gap:6px}
  .benefits svg{width:22px;height:22px}
  .contact--back{left:20px;top:478px;display:flex;flex-wrap:wrap;width:380px;column-gap:18px}
</style>
</head>
<body>

<section class="card card--front">
  <svg class="art" width="690" height="535" viewBox="0 0 690 535">
    <defs>
      <linearGradient id="orangeFade" x1="0" y1="0" x2="1" y2="1">
        <stop offset="0" stop-color="var(--orange-light)"/><stop offset="1" stop-color="var(--orange)"/>
      </linearGradient>
      <linearGradient id="blueFade" x1="0" y1="0" x2="1" y2="0">
        <stop offset="0" stop-color="var(--blue)"/><stop offset=".6" stop-color="var(--blue-light)"/><stop offset="1" stop-color="var(--blue)"/>
      </linearGradient>
      <linearGradient id="photoFade" x1="0" y1="0" x2="0" y2="1">
        <stop offset="0" stop-color="var(--photo-a)"/><stop offset="1" stop-color="var(--photo-b)"/>
      </linearGradient>
    </defs>
    <path role="img" aria-label="Photo of a smiling woman with arms crossed" d="M400,125 H690 V535 H470 C420,430 430,260 400,125 Z" fill="url(#photoFade)"/>
    <path d="M0,100 C120,70 260,80 330,120 C390,160 380,300 420,420 C440,480 455,510 470,535 H0 Z" fill="url(#orangeFade)"/>
    <path d="M330,120 C390,160 380,300 420,420 C440,480 455,510 470,535" fill="none" stroke="var(--dark)" stroke-width="9"/>
    <path d="M345,112 C405,160 400,300 440,420 C460,480 475,510 495,535" fill="none" stroke="var(--blue)" stroke-width="5"/>
    <path d="M0,0 H690 V66 C560,88 420,102 300,84 C190,68 90,72 0,96 Z" fill="url(#blueFade)"/>
    <path d="M0,96 C90,72 190,68 300,84 C420,102 560,88 690,66" fill="none" stroke="var(--dark)" stroke-width="6"/>
    <path d="M320,98 C450,110 580,100 690,82" fill="none" stroke="var(--yellow)" stroke-width="4"/>
    <path d="M0,330 C160,315 320,330 390,390 C430,430 450,490 480,535 H0 Z" fill="url(#blueFade)"/>
    <path d="M0,455 C170,445 320,470 440,535 H0 Z" fill="var(--dark)"/>
    <path d="M0,455 C170,445 320,470 440,535" fill="none" stroke="var(--white)" stroke-width="3"/>
  </svg>
  <div class="txt formula">N2O</div>
  <h1 class="txt title title--nitrous">Nitrous</h1>
  <div class="txt title title--oxide">OXIDE</div>
  <div class="txt title title--inhaler">INHALER</div>
  <div class="product-shot" role="img" aria-label="Photo of the handheld nitrous oxide inhaler"></div>
  <div class="txt plus">+</div>
  <div class="txt painful">YOUR PAINFUL</div>
  <div class="txt procedure">PROCEDURE</div>
  <div class="txt equals">=</div>
  <div class="txt reduce">Reduce PAIN and ANXIETY</div>
  <div class="txt seconds">In seconds</div>
  <ul class="contact contact--front">
    <li><svg viewBox="0 0 16 16"><path d="M4 1l3 3-2 2c1 2 3 4 5 5l2-2 3 3-2 3C7 15 1 9 1 3z" fill="var(--yellow)"/></svg>1-555-014-0392</li>
    <li><svg viewBox="0 0 16 16"><rect x="1" y="3" width="14" height="10" fill="var(--yellow)"/><path d="M1 3l7 6 7-6" stroke="var(--dark)" fill="none"/></svg>ridgefoxcare@mail.com</li>
    <li><svg viewBox="0 0 16 16"><circle cx="8" cy="8" r="7" fill="var(--yellow)"/></svg>www.ridgefoxparts.com</li>
  </ul>
</section>

<section class="card card--back">
  <svg class="art" width="690" height="535" viewBox="0 0 690 535">
    <defs>
      <linearGradient id="orangeBack" x1="0" y1="0" x2="1" y2="1">
        <stop offset="0" stop-color="var(--orange-light)"/><stop offset="1" stop-color="var(--orange)"/>
      </linearGradient>
      <linearGradient id="photoBack" x1="0" y1="0" x2="1" y2="0">
        <stop offset="0" stop-color="#d8b8a4"/><stop offset="1" stop-color="#c9c6bd"/>
      </linearGradient>
    </defs>
    <path d="M0,0 H250 C320,10 360,60 365,140 V475 H0 Z" fill="url(#orangeBack)"/>
    <rect x="0" y="105" width="355" height="3" fill="var(--white)"/>
    <rect role="img" aria-label="Photo of a woman using the handheld inhaler" x="0" y="110" width="355" height="250" fill="url(#photoBack)"/>
    <rect x="0" y="360" width="355" height="3" fill="var(--white)"/>
    <path d="M260,0 C340,20 370,80 372,160 V440 C372,460 378,470 390,475" fill="none" stroke="var(--dark)" stroke-width="10"/>
    <path d="M280,0 C355,25 385,85 387,165 V440 C387,455 395,468 410,475" fill="none" stroke="var(--blue)" stroke-width="6"/>
    <path d="M0,475 H395 L475,500 V535 H0 Z" fill="var(--dark)"/>
  </svg>
  <h2 class="txt ask">ASK YOUR NURSE</h2>
  <div class="txt ask-sub">FOR AVAILABILITY AND PRICING</div>
  <p class="blurb">Hand held nitrous oxide inhaler used to put patients at ease before painful procedures</p>
  <div class="txt benefits">
    <span><svg viewBox="0 0 20 20"><path d="M2 11l5 5L18 3" stroke="var(--blue)" stroke-width="4" fill="none"/></svg>Safe</span>
    <span><svg viewBox="0 0 20 20"><path d="M2 11l5 5L18 3" stroke="var(--blue)" stroke-width="4" fill="none"/></svg>Fast</span>
    <span><svg viewBox="0 0 20 20"><path d="M2 11l5 5L18 3" stroke="var(--blue)" stroke-width="4" fill="none"/></svg>Easy</span>
  </div>
  <ul class="contact contact--back">
    <li><svg viewBox="0 0 16 16"><path d="M4 1l3 3-2 2c1 2 3 4 5 5l2-2 3 3-2 3C7 15 1 9 1 3z" fill="var(--yellow)"/></svg>1-555-014-0392</li>
    <li><svg viewBox="0 0 16 16"><rect x="1" y="3" width="14" height="10" fill="var(--yellow)"/><path d="M1 3l7 6 7-6" stroke="var(--dark)" fill="none"/></svg>ridgefoxcare@mail.com</li>
    <li><svg viewBox="0 0 16 16"><circle cx="8" cy="8" r="7" fill="var(--yellow)"/></svg>www.ridgefoxparts.com</li>
  </ul>
</section>

</body>
</html>
```